Corvella Website Homepage

Committed to delivering quality content, quillpagewords.com is a content providing company. Equipped with resourceful writers with industry experience, we promise to empower our clients with content that is tailor-made to address specific requirements of their target Audience.

We need a website home page and one internal page designed. It is very important that the page be laid out with SEO in mind. We like the idea of using five images as navigation to our services. The five major services we offer are:
• Web Content writing (articles, features, website copy etc)
• Business Content writing (Press release, mailers & flyers, brochure/catalog)
• Personal Content writing (blog, speech writing)
• Hire a writer/editor
• Proof reading and editing services
The sample template (http://pv7.layoutdemo-hub.net/dx_48270/index.html) included has five images in the first fold. Designer can choose the right image for each service and lay over the service name on the image. Please do not use flash ( We will use javascripts). We need to have a detailed right side nav as in the template for SEO reasons. There will be some marketing ad- copy below the main images. Followed by a 200 character SEO optimized text defining our services in further detail. Apart from these a designer is free to use his creativity. The name of the site will be http://www.quillpagewords.com/. This name will need a logo too. Please include it as part of design. Corvellacorp is the owner of quillpagewords.com. We already have a logo for Corvella that is attached here as a separate file.

We have some taglines that need to be incorporated in the home page and other pages.
Please provide link button for Home, About us, Services, Samples, Pricing, Clients, Career, Contact us.

Links can be given on TOP, Sideways and Bottom and in the drop down menu of services etc.

Reason: Hi

We have made our project guaranteed and extended deadline by 5 days so you get more time to complete our project.

Thanks and Regards,

Ravindra Kulkarni
Corvellacorp

Target Market(s)

Product Marketing Companies - Mostly in US.
Media companies which publish articles on various subjects. Travel and Lifestyle related sites, Educational Websites, Government Websites, Health related websites,

Industry/Entity Type

Marketing

Requirements
Must have
• Color of Homepage should blend with sober mood of the content. Writing Services should get highlighted in such a way that any person serious about the business visiting the site get attracted to read on the details of our content services. Most space should be used for details of writing services and links for our various pages and services. Webpage should be downloaded in lowest possible time.
Nice to have
• We have some idea about the website layouts;-http://www.skinbazaarly.net/site-layouts/48270.html - layout of information http://www.skinbazaarly.net/site-layouts/47359.html - for kind of marketing http://pv7.layoutdemo-hub.net/dx_48615/index.html - for colors
we attach a word file representing our idea in some way but not limited to it.
Should not have
• Gaudy (aggressive dark) colors. It should not be cluttered. No flash.

```html
<!DOCTYPE html>
<html lang="en">
<head>
<meta charset="utf-8">
<title>QuillPageWords.com – Our values</title>
<link rel="stylesheet" href="https://fonts.googleapis.com/css2?family=Arimo:ital,wght@0,400;0,700;1,400&family=Open+Sans:ital,wght@0,400;0,600;1,400;1,600&display=swap">
<style>
:root{
  --blue:#2a8fd8;
  --blue-deep:#1c72b8;
  --navy:#17557f;
  --link:#2f86c8;
  --text:#6b8aa3;
  --rule:#d9e3ea;
  --white:#ffffff;
}
*{margin:0;padding:0;box-sizing:border-box}
html,body{width:807px;height:1200px;overflow:hidden;background:var(--white)}
body{position:relative;font-family:Arimo,Arial,sans-serif;color:var(--text)}
.abs{position:absolute}
.top-strip{left:0;top:0;width:807px;height:7px;background:var(--blue)}
.brand{left:70px;top:31px;display:flex;align-items:center;gap:8px}
.brand-name{font-family:"Open Sans",sans-serif;font-weight:600;font-size:20px;color:var(--blue)}
.brand-dot{width:22px;height:22px;border-radius:50%;background:var(--blue)}
.nav{left:0;top:76px;width:807px;height:38px;background:linear-gradient(#3aa0e6,#248bd6)}
.nav ul{list-style:none;display:flex;position:absolute;left:60px;top:0;height:38px}
.nav li{font-family:"Open Sans",sans-serif;font-size:11px;color:var(--white);padding:0 10px;line-height:38px;border-left:1px solid rgba(255,255,255,.35)}
.nav li:first-child{border-left:none}
.nav li.current{background:#3fa8ee}
.hero{left:0;top:114px;width:807px;height:116px;background:linear-gradient(100deg,#3d9de3 0%,#4aa6ea 45%,#3a98e0 100%)}
.hero h1{position:absolute;left:70px;top:40px;font-size:27px;font-weight:700;color:var(--white)}
.crumbs{position:absolute;left:72px;top:94px;font-size:9.5px;font-weight:700;color:#d8ecfb}
.crumbs b{color:var(--white)}
.sidebar{left:591px;top:230px;width:216px;height:520px;background:linear-gradient(90deg,#eef3f6,#fafcfd 20%,#fff);-webkit-mask-image:linear-gradient(#000 75%,transparent);mask-image:linear-gradient(#000 75%,transparent)}
.side-title{left:626px;top:248px;font-size:15px;font-weight:700;color:#5f7584}
.offer{left:626px;top:276px;width:143px;list-style:none}
.offer li{font-size:10.5px;color:var(--link);height:19.2px;line-height:18px;border-bottom:1px solid var(--rule);padding-left:10px;position:relative}
.offer li:last-child{border-bottom:none}
.offer li::before{content:"";position:absolute;left:0;top:6px;border-left:5px solid #4a5a66;border-top:3px solid transparent;border-bottom:3px solid transparent}
.career{left:604px;top:536px;width:164px;height:166px;border-radius:6px;background:linear-gradient(#4aaaf0,#2a8ad6);text-align:center;font-family:"Open Sans",sans-serif;color:var(--white)}
.career .kicker{margin-top:16px;font-size:10px;font-style:italic;font-weight:600;color:#123d5e}
.career .label{margin:5px 13px 0;height:28px;line-height:28px;background:#5cb6f1;font-size:17px;font-weight:600}
.career p{margin:9px 12px 0;font-size:10px;font-style:italic;line-height:16px}
.career-glow{left:604px;top:704px;width:164px;height:38px;border-radius:0 0 6px 6px;background:linear-gradient(#d6e9f7,rgba(255,255,255,0))}
.page-title{left:70px;top:244px;font-size:19px;font-weight:700;color:var(--navy)}
.lead{left:70px;top:274px;width:508px;font-size:15px;line-height:21.5px;color:#6f93b0}
.subhead{left:70px;top:352px;font-size:15px;font-weight:400;color:var(--link)}
.copy{left:70px;top:382px;width:490px;font-size:9.4px;line-height:13px;color:#7f97ac}
.fade-rule{left:70px;top:474px;width:490px;height:1px;background:linear-gradient(90deg,rgba(220,230,238,0),#e0e8ee 40%,rgba(220,230,238,0))}
.value{width:190px}
.value .icon{position:absolute;left:0;top:0;width:36px;height:36px;border-radius:8px}
.value h3{position:absolute;left:54px;top:0;font-size:11.5px;font-weight:700;color:var(--link)}
.value p{position:absolute;left:54px;top:16px;width:180px;font-size:9.4px;line-height:12.8px;color:#7d8b96}
.rule{left:70px;top:887px;width:484px;height:1px;background:var(--rule)}
.btn{font-size:9.5px;font-weight:700;color:var(--white);text-align:center;background:linear-gradient(#2f96e0,#1c7bc8)}
.cta{left:70px;top:902px;width:101px;height:21px;line-height:21px}
.banner{left:39px;top:959px;width:729px;height:112px;border-radius:7px;background:linear-gradient(90deg,#cfe4f4,#eef6fc 55%,#e3f0fa)}
.banner-photo{left:180px;top:915px;width:197px;height:156px;background:linear-gradient(160deg,#6a8fc0,#c9d6e3 60%,#2f3a46)}
.banner-title{left:388px;top:1000px;font-family:"Open Sans",sans-serif;font-size:24px;font-weight:600;color:var(--navy);white-space:nowrap}
.banner-tag{left:388px;top:1033px;font-family:"Open Sans",sans-serif;font-style:italic;font-size:14px;color:var(--blue-deep)}
.learn{left:647px;top:1028px;width:101px;height:21px;line-height:21px}
.footer{left:0;top:1097px;width:807px;height:103px;background:linear-gradient(#eef4f8,#f8fbfd)}
.foot-links{left:70px;top:1112px;font-size:9.5px;color:#2a4b63}
.foot-links u{color:var(--link)}
.copyright{left:70px;top:1160px;font-size:9.5px;color:#5a6a76}
.news-title{left:531px;top:1111px;font-size:11px;font-weight:700;color:#2a4b63}
.news-icon{left:600px;top:1112px}
.email{left:531px;top:1135px;width:155px;height:16px;border:1px solid #c9d5dd;background:var(--white);font-size:9px;font-style:italic;color:#a8b4bd;padding:2px 12px;line-height:11px}
.subscribe{left:699px;top:1135px;width:60px;height:16px;line-height:16px}
.social{left:531px;top:1161px;display:flex;align-items:center;gap:8px;font-size:9.5px;font-weight:700;color:#4a6a80}
.social .follow{color:var(--link)}
.social i{display:inline-block;width:10px;height:10px;background:#3a6eb0}
.social i.tw{background:#8fc7ec}
</style>
</head>
<body>
<div class="abs top-strip"></div>
<header>
  <div class="abs brand"><span class="brand-name">QuillPageWords.com</span><span class="brand-dot"></span></div>
  <nav class="abs nav"><ul>
    <li>HOME</li><li class="current">ABOUT US</li><li>SERVICES</li><li>SAMPLES</li><li>PRICING</li><li>CLIENTS</li><li>CAREER</li><li>CONTACT US</li>
  </ul></nav>
  <section class="abs hero">
    <h1>Our values</h1>
    <div class="crumbs">Home / Parent directory / Second parent / <b>About us</b></div>
  </section>
</header>

<aside>
  <div class="abs sidebar"></div>
  <h3 class="abs side-title">What we offer</h3>
  <ul class="abs offer">
    <li>Urgent Translation</li><li>Legal Translation</li><li>Patent Translation</li><li>Medical Translation</li><li>Technical Translation</li><li>Marketing Translation</li><li>Financial Translation</li><li>Persosal Translation</li><li>Website Translation</li><li>Proofreading</li><li>Transcription</li><li>Voiceovers</li>
  </ul>
  <div class="abs career">
    <div class="kicker">become part of our team</div>
    <div class="label">Career center</div>
    <p>Quisque ultricies congue mauris, at consectetur nunc ornare sed. Cras nibh erat, amet, consectetur adipiscing elit.</p>
  </div>
  <div class="abs career-glow"></div>
</aside>

<main>
  <h2 class="abs page-title">What we trust in?</h2>
  <p class="abs lead">Lorem ipsum dolor sit amet, consectetur adipiscing elit. Curabitur congue erat et massa eleifend gravida. Nunc nisl purus, iaculis vitae posuere non, malesuada nec metus. Vestibulum vel neque nunc.</p>
  <h3 class="abs subhead">Lorem ipsum dolor sit amet, consectetur adipiscing elit</h3>
  <p class="abs copy">Lorem ipsum dolor sit amet, consectetur adipiscing elit. Maecenas varius felis sed turpis facilisis vel auctor ante rutrum. Aliquam ornare fringilla justo, aliquam semper sapien aliquet in. Aliquam gravida, risus in consectetur mattis, ante orci placerat nulla, a condimentum risus nunc sit amet nibh. Sed vitae mollis ligula. Ut ut.Aliquam dapibus cursus accumsan. Integer auctor elementum eros, bibendum hendrerit metus gravida nec. Vivamus vitae varius felis. Phasellus lectus mi, varius sed placerat quis, imperdiet a arcu. Duis ac justo eros, in blandit felis. Duis vitae quam nulla, quis facilisis velit. Nullam congue, lorem sit amet accumsan consectetur, eros lorem.</p>
  <div class="abs fade-rule"></div>

  <div class="abs value" style="left:70px;top:491px">
    <div class="icon" role="img" aria-label="Gold star icon" style="background:#f3cf4a"></div>
    <h3>Quality</h3>
    <p>Suspendisse potenti. Phasellus vitae velit velit, nec vehicula metus. Suspendisse malesuada elementum suscipit. Duis rutrum pretium consequat. Vivamus scelerisque mollis nibh vel auctor.</p>
  </div>
  <div class="abs value" style="left:327px;top:491px">
    <div class="icon" role="img" aria-label="Pencil icon" style="background:#eab65a"></div>
    <h3>Expertise</h3>
    <p>Suspendisse potenti. Phasellus vitae velit velit, nec vehicula metus. Suspendisse malesuada elementum suscipit. Duis rutrum pretium consequat. Vivamus scelerisque.</p>
  </div>
  <div class="abs value" style="left:70px;top:594px">
    <div class="icon" role="img" aria-label="Crossed pencil and brush icon" style="background:#a6c75e"></div>
    <h3>Creativity</h3>
    <p>Suspendisse potenti. Phasellus vitae velit velit, nec vehicula metus. Suspendisse malesuada elementum suscipit. Duis rutrum pretium consequat. Vivamus.</p>
  </div>
  <div class="abs value" style="left:327px;top:594px">
    <div class="icon" role="img" aria-label="Businessman icon" style="background:#8a4a44"></div>
    <h3>Integrity</h3>
    <p>Suspendisse potenti. Phasellus vitae velit velit, nec vehicula metus. Suspendisse malesuada elementum suscipit. Duis rutrum pretium .</p>
  </div>
  <div class="abs value" style="left:70px;top:697px">
    <div class="icon" role="img" aria-label="Open hand icon" style="background:#e9c9a4"></div>
    <h3>Delivery</h3>
    <p>Suspendisse potenti. Phasellus vitae velit velit, nec vehicula metus. Suspendisse malesuada elementum suscipit. Duis rutrum pretium consequat. Vivamus scelerisque mollis nibh.</p>
  </div>
  <div class="abs value" style="left:327px;top:697px">
    <div class="icon" role="img" aria-label="Magician hat icon" style="background:#3a2f33"></div>
    <h3>Originality</h3>
    <p>Suspendisse potenti. Phasellus vitae velit velit, nec vehicula metus. Suspendisse malesuada elementum suscipit. Duis rutrum pretium .</p>
  </div>
  <div class="abs value" style="left:70px;top:800px">
    <div class="icon" role="img" aria-label="Globe icon" style="background:#5d9bd4;border-radius:50%"></div>
    <h3>Service</h3>
    <p>Suspendisse potenti. Phasellus vitae velit velit, nec vehicula metus. Suspendisse malesuada elementum suscipit. Duis rutrum pretium consequat.</p>
  </div>

  <div class="abs rule"></div>

  <section>
    <div class="abs banner"></div>
    <div class="abs banner-photo" role="img" aria-label="Photo of a writer in a blue shirt working at a laptop"></div>
    <h2 class="abs banner-title">Hire a writer or editor</h2>
    <div class="abs banner-tag">Choose the right message!</div>
    <div class="abs btn learn">Learn more</div>
  </section>
  <div class="abs btn cta">Contact us for more</div>
</main>

<footer>
  <div class="abs footer"></div>
  <div class="abs foot-links">Home | About us | <u>Services</u> | Samples | Pricing | Clients | Career | Contact us</div>
  <div class="abs copyright">Copyright 2011 © QuillPageWords.com</div>
  <div class="abs news-title">Newsletter</div>
  <svg class="abs news-icon" width="12" height="9" viewBox="0 0 12 9"><rect x="0.5" y="0.5" width="11" height="8" fill="none" stroke="#2f86c8"/><path d="M0.5 0.5 6 5 11.5 0.5" fill="none" stroke="#2f86c8"/></svg>
  <div class="abs email">your e-mail</div>
  <div class="abs btn subscribe">Subscribe</div>
  <div class="abs social"><span>Become a fan</span><i></i><span class="follow">Follow us</span><i class="tw"></i></div>
</footer>
</body>
</html>
```